Business Card Design

We need a business card design for a kids clothes shop in Ireland called "Tiny Trotz". Would prefer the colours Lime Green and Dark Purple to be used but are open to suggestions. The logo should include a "Cool" penguin with clothes on.

Industry/Entity Type

Shop

Contact Information for Business Card

Tiny Trotz
Harlow Arcade,
Ashvale Road, Childrenswear 0-12yrs
Kilbrannagh,
XQ82 5LW. Deirdre Walsh.

```html
<!DOCTYPE html>
<html lang="en">
<head>
<meta charset="utf-8">
<title>Tiny Trotz – Business Card</title>
<link rel="stylesheet" href="https://fonts.googleapis.com/css2?family=Archivo+Black&family=Questrial&display=swap">
<style>
  :root {
    --page-bg: #dcdcdc;
    --card-bg: #f2f2f2;
    --card-bg-shade: #e4e4e4;
    --ice-blue: #a8dde8;
    --penguin-black: #1f1d1e;
    --sweater-blue: #cdebf1;
    --scarf-lime: #b5d56a;
    --scarf-purple: #2f2a7a;
  }
  * { box-sizing: border-box; margin: 0; padding: 0; }
  html, body {
    width: 1200px;
    height: 1000px;
    overflow: hidden;
    background: var(--page-bg);
  }
  .canvas {
    position: relative;
    width: 1200px;
    height: 1000px;
    display: flex;
    align-items: center;
    justify-content: center;
  }
  .business-card {
    position: relative;
    width: 900px;
    height: 514px;
    background: linear-gradient(135deg, var(--card-bg) 0%, var(--card-bg-shade) 100%);
    box-shadow: 0 6px 18px rgba(0, 0, 0, 0.18);
  }
  .mascot-art {
    position: absolute;
    left: 130px;
    top: 60px;
    width: 320px;
    height: 400px;
    border-radius: 40% 40% 30% 30% / 30% 30% 25% 25%;
    background: linear-gradient(180deg,
      var(--penguin-black) 0%,
      var(--scarf-lime) 22%,
      var(--sweater-blue) 45%,
      var(--sweater-blue) 62%,
      var(--penguin-black) 100%);
  }
  .shop-name {
    position: absolute;
    left: 460px;
    top: 70px;
    width: 360px;
    font-family: "Archivo Black", sans-serif;
    font-size: 84px;
    line-height: 0.95;
    color: var(--ice-blue);
    text-align: center;
  }
  .shop-name span { display: block; }
  .shop-details {
    position: absolute;
    left: 450px;
    top: 340px;
    width: 380px;
    font-family: "Questrial", sans-serif;
    font-size: 18px;
    line-height: 1.25;
    color: var(--ice-blue);
    text-align: center;
  }
  .shop-details p { margin: 0; }
</style>
</head>
<body>
  <main class="canvas">
    <section class="business-card">
      <div class="mascot-art" role="img" aria-label="Illustration of a cartoon penguin wearing a light blue jumper and a lime green scarf with purple stripes"></div>

      <h1 class="shop-name">
        <span>Tiny</span>
        <span>Trotz</span>
      </h1>

      <address class="shop-details">
        <p>Tiny Trotz - Childrenswear 0-12yrs</p>
        <p>Harlow Arcade, Ashvale Road,</p>
        <p>Kilbrannagh, XQ82 5LW</p>
        <p>Deirdre Walsh</p>
      </address>
    </section>
  </main>
</body>
</html>
```